Odvetnik - Attorney at law
Sodni tolmač za angleški jezik - English language Court Interpreter
Simple
Marjan Lesk
Odvetnik - Attorney at law Sodni tolmač za angleški jezik - English Language Court Interpreter
Brinjeva ulica 41 6000 Koper Slovenija
info@marjanlesk.example
www.marjanlesk.example
I invite all designers under logo project Attorney Marjan Lesk to participate. Please inform all designers.

```html
<!DOCTYPE html>
<html lang="sl">
<head>
<meta charset="utf-8">
<title>Marjan Lesk – Odvetnik</title>
<link rel="stylesheet" href="https://fonts.googleapis.com/css2?family=Source+Sans+3:wght@400;600;700&display=swap">
<style>
  :root {
    --page-bg: #e6e6e8;
    --card-white: #ffffff;
    --card-indigo: #48468e;
    --accent-orange: #ef7d22;
    --ink-navy: #2f2f6e;
    --text-light: #ffffff;
    --rule-light: rgba(255,255,255,0.75);
  }
  * { box-sizing: border-box; margin: 0; padding: 0; }
  html, body {
    width: 1200px; height: 780px; overflow: hidden;
    background: var(--page-bg);
    font-family: "Source Sans 3", "Helvetica Neue", Arial, sans-serif;
  }
  .canvas {
    position: relative; width: 1200px; height: 780px;
    display: flex; align-items: center; justify-content: center;
  }
  .business-card {
    width: 900px; height: 560px;
    border-radius: 38px;
    overflow: hidden;
    background: var(--card-white);
    display: flex; flex-direction: column;
    box-shadow: 0 10px 30px rgba(0,0,0,0.18);
  }
  .card-top {
    height: 262px;
    display: flex; flex-direction: column; align-items: center; justify-content: center;
    padding-top: 30px;
  }
  .brand {
    display: flex; align-items: center; gap: 18px;
  }
  .brand-dot {
    width: 54px; height: 54px; border-radius: 50%;
    background: var(--accent-orange);
  }
  .brand-name {
    font-size: 64px; font-weight: 600; letter-spacing: 1px;
    color: var(--ink-navy); line-height: 1;
  }
  .brand-tagline {
    margin-top: 10px; margin-left: 72px;
    font-size: 23px; color: var(--ink-navy); letter-spacing: 0.5px;
  }
  .accent-line {
    height: 6px; background: var(--accent-orange);
    border-bottom: 3px solid var(--card-white);
    box-sizing: content-box;
  }
  .card-bottom {
    flex: 1; background: var(--card-indigo); color: var(--text-light);
    display: flex; flex-direction: column; align-items: center;
    padding-top: 40px;
  }
  .role-title {
    font-size: 31px; font-weight: 600; line-height: 1.3; text-align: center;
  }
  .divider {
    width: 620px; height: 1px; background: var(--rule-light);
    margin: 22px 0 18px;
  }
  .contact {
    font-size: 21px; line-height: 1.55; text-align: center;
  }
  .contact b { font-weight: 700; }
  .contact span + span { margin-left: 22px; }
</style>
</head>
<body>
  <main class="canvas">
    <article class="business-card">
      <header class="card-top">
        <div class="brand">
          <span class="brand-dot"></span>
          <span class="brand-name">MARJAN LESK</span>
        </div>
        <p class="brand-tagline">Odvetnik - Attorney at law</p>
      </header>
      <div class="accent-line"></div>
      <section class="card-bottom">
        <h1 class="role-title">Sodni tolmač za angleški jezik<br>English Language Court Interpreter</h1>
        <div class="divider"></div>
        <address class="contact" style="font-style:normal">
          <p><span><b>T:</b> +386 5 6102340</span><span><b>M:</b> +386 41552870</span><span><b>F:</b> +386 5 6102341</span></p>
          <p><span><b>E:</b> info@marjanlesk.example</span><span><b>W:</b> www.marjanlesk.example</span></p>
          <p>Brinjeva ulica 41, 6000 Koper, Slovenija</p>
        </address>
      </section>
    </article>
  </main>
</body>
</html>
```